Website for School Supplies Business

We are rebuilding this website: http://ashfordlane.example/ and need a new professional design template created. The site will be built on Shopify so it should work on this platform. Also it should be "responsive-ready" so the developer can make it work on many devices.

Ashford Lane (AL) is a very well respected and trusted school supplies business in Australia. It has been around in Australia for over 20 years, and is widely known and trusted by teachers. You can see their product range on the current website.

The current website, including the logo now looks outdated. There is no need to include the current logo on the template design and we want designs that are not so oriented towards kids. Whilst they sell school supplies the users of the website will be teachers. We would prefer an professional friendly look rather than a kidsy style. In terms of colours we suggest bright and light colours should feature - whilst still keeping a professional, elegant look.

Most of their current orders are made by phone / fax. The teachers look at the catalog (they have physical copies at the school) and then place their orders. A lesser number come through the website but that number will increase significantly over the next year or 2. This new website is to take advantage of this trend towards online orders.

Typically the schools are placing orders for multiple items at once. They will often know what they want to order in advance as they have catalogs. It is very important that it is easy to find items on the site (searching by product name or product code) and it must be easy to order multiple items. The current website has a heavy emphasis on the online catalogs. Whilst we still want these available on the site, we want the focus on these reduced.

We expect the category structure to be quite similar to the current site.

We want the homepage to include an area where there blog posts are shown.

Deliverables include:

1. Homepage design
2. Product page design
3. Category page design
4. Info page design (About Us etc.)

We look forward to your designs!
Updates

Target Market(s)

Australian primary school teachers.

Industry/Entity Type

School

Colors

Designer to choose colors to be used in the design.

Requirements
Must have
• Strong search functionality.

```html
<!DOCTYPE html>
<html lang="en">
<head>
<meta charset="utf-8">
<title>Ashford Lane – School Supplies</title>
<link href="https://fonts.googleapis.com/css2?family=Open+Sans:wght@400;600;700&display=swap" rel="stylesheet">
<style>
:root{
  --orange:#f26b21;
  --blue:#2b7bbf;
  --ink:#333;
  --muted:#888;
  --line:#e3e3e3;
  --hero:#eeeeee;
  --footer:#3a3a3a;
  --footer-deep:#2c2c2c;
  --black:#111;
}
*{box-sizing:border-box;margin:0;padding:0}
html,body{width:764px;height:1200px;overflow:hidden;background:#fff}
body{font-family:"Open Sans",Arial,sans-serif;color:var(--ink);font-size:8px}
.wrap{width:616px;margin:0 auto;position:relative}

.topbar{height:20px;border-bottom:1px solid var(--line);font-size:6.5px;color:var(--muted)}
.topbar .wrap{display:flex;justify-content:space-between;align-items:center;height:20px}
.topbar nav span{margin-right:10px}
.cart-total b{display:inline-block;border:1px solid var(--line);padding:1px 5px;margin-left:4px;font-weight:400}

.masthead .wrap{height:50px;display:flex;justify-content:space-between;align-items:center}
.brand-name{font-size:20px;font-weight:700;color:var(--ink);line-height:1}
.brand-tag{font-size:7px;color:var(--muted);margin-top:2px}
.search{width:120px;height:16px;border:1px solid var(--line);font-size:6px;color:#aaa;padding:0 6px;display:flex;align-items:center;justify-content:space-between}

.mainnav{border-bottom:1px solid var(--line)}
.mainnav .wrap{display:flex;gap:34px;height:22px;align-items:center;font-size:8px;color:var(--muted)}
.mainnav .active{color:var(--blue);border-bottom:2px solid var(--blue);padding-bottom:3px}

.hero{background:var(--hero);height:212px;margin-top:4px}
.hero .wrap{height:212px}
.hero-copy{position:absolute;left:0;top:54px;width:240px}
.hero h1{font-size:17px;font-weight:700;color:var(--ink)}
.hero p{font-size:8px;color:#666;margin-top:6px;line-height:1.4}
.btn{display:inline-block;background:var(--orange);color:#fff;font-weight:600}
.hero .btn{font-size:11px;padding:6px 11px;margin-top:12px}
.hero-art{position:absolute;right:30px;top:14px;width:230px;height:180px;background:linear-gradient(135deg,#f7d23b,#4ba3e0 45%,#e8407a 80%,#7dc242)}
.dots{position:absolute;left:0;bottom:10px;display:flex;gap:5px}
.dots i{width:5px;height:5px;border-radius:50%;background:#999}

.features{display:flex;gap:24px;margin-top:28px}
.feature{width:189px;text-align:center}
.feature .thumb{height:100px}
.feature h3{font-size:12px;font-weight:400;margin-top:6px}
.feature p{font-size:6.5px;color:#666;line-height:1.35;margin-top:3px;padding:0 10px}
.feature .btn{font-size:6.5px;padding:4px 9px;margin-top:8px}

.section-head{display:flex;justify-content:space-between;align-items:center;margin-top:28px}
.section-head h2{font-size:11px;font-weight:400}
.arrows{display:flex;gap:3px}
.arrows svg{width:11px;height:11px}

.products{display:grid;grid-template-columns:repeat(4,142px);gap:20px 16px;margin-top:12px}
.product .thumb{height:135px;border:1px solid var(--line);background:#fff;display:flex;align-items:center;justify-content:center}
.product .thumb div{width:80px;height:90px}
.product .name{font-size:6.5px;font-weight:600;text-align:right;border-bottom:1px solid var(--line);padding:5px 0 4px;text-transform:uppercase}
.product .row{display:flex;justify-content:space-between;align-items:center;margin-top:5px}
.price{font-size:7.5px;font-weight:600}
.add{background:var(--black);color:#fff;font-size:5px;font-weight:700;padding:3px 5px}

.footer{background:var(--footer);color:#ccc;position:absolute;left:0;top:990px;width:764px;height:190px}
.footer .wrap{display:flex;gap:24px;padding-top:16px}
.footer h4{font-size:7px;font-weight:600;color:#fff;text-transform:uppercase;margin-bottom:8px}
.col{width:136px;font-size:6px;line-height:1.5}
.contact li{list-style:none;display:flex;gap:6px;align-items:flex-start;margin-bottom:5px}
.contact svg{width:8px;height:8px;flex:none;margin-top:1px}
.tweet{margin-bottom:8px}
.gallery{display:grid;grid-template-columns:repeat(3,38px);gap:4px}
.gallery div{height:30px}
.legal{position:absolute;left:0;top:1180px;width:764px;height:20px;background:var(--footer-deep);color:#aaa;font-size:6px;display:flex;align-items:center;justify-content:center}
</style>
</head>
<body>

<header>
  <div class="topbar"><div class="wrap">
    <nav><span>My Account</span><span>My Cart</span><span>Checkout</span><span>Login</span></nav>
    <div class="cart-total">Shopping Cart <b>$0.00</b></div>
  </div></div>

  <div class="masthead"><div class="wrap">
    <div class="brand">
      <div class="brand-name">Ashford Lane</div>
      <div class="brand-tag">Bright ideas for your classroom</div>
    </div>
    <div class="search"><span>Search here</span>
      <svg width="7" height="7" viewBox="0 0 10 10"><circle cx="4" cy="4" r="3" fill="none" stroke="#999" stroke-width="1.3"/><line x1="6.2" y1="6.2" x2="9" y2="9" stroke="#999" stroke-width="1.3"/></svg>
    </div>
  </div></div>

  <nav class="mainnav"><div class="wrap">
    <span class="active">Home</span><span>About Us</span><span>Contact Us</span><span>Sign In</span><span>Wish List</span><span>Freight Charges</span>
  </div></nav>
</header>

<section class="hero"><div class="wrap">
  <div class="hero-copy">
    <h1>NEW 2014 CATALOGUE</h1>
    <p>Lorem ipsum dolor sit amet, consectetur adipiscing elit, sed do eiusmod tempor incididunt ut labore et dolore magna aliqua.</p>
    <span class="btn">Order Now</span>
  </div>
  <div class="hero-art" role="img" aria-label="Colourful stack of folders, binders and pencils"></div>
  <div class="dots"><i></i><i></i><i></i></div>
</div></section>

<main class="wrap">
  <section class="features">
    <article class="feature">
      <div class="thumb" role="img" aria-label="Toddler playing with toys" style="background:linear-gradient(135deg,#c9d9e8,#e9c9a0)"></div>
      <h3>Child Toy</h3>
      <p>Lorem ipsum dolor sit amet, consectetur adipiscing elit, sed diam nonummy nibh euismod tincidunt.</p>
      <span class="btn">Read More</span>
    </article>
    <article class="feature">
      <div class="thumb" role="img" aria-label="Classroom book storage shelves" style="background:linear-gradient(135deg,#e6e6e6,#a9c7e0 50%,#e8b04a)"></div>
      <h3>Book storage &amp; display</h3>
      <p>Lorem ipsum dolor sit amet, consectetur adipiscing elit, sed diam nonummy nibh euismod tincidunt.</p>
      <span class="btn">Read More</span>
    </article>
    <article class="feature">
      <div class="thumb" role="img" aria-label="Child drawing at a desk" style="background:linear-gradient(135deg,#f0ece6,#d9c2a8)"></div>
      <h3>Classroom Essentials</h3>
      <p>Lorem ipsum dolor sit amet, consectetur adipiscing elit, sed diam nonummy nibh euismod tincidunt.</p>
      <span class="btn">Read More</span>
    </article>
  </section>

  <div class="section-head">
    <h2>NEW PRODUCTS</h2>
    <div class="arrows">
      <svg viewBox="0 0 12 12"><rect width="12" height="12" fill="#ddd"/><path d="M7 3 4 6l3 3" fill="none" stroke="#fff" stroke-width="1.5"/></svg>
      <svg viewBox="0 0 12 12"><rect width="12" height="12" fill="#ddd"/><path d="M5 3l3 3-3 3" fill="none" stroke="#fff" stroke-width="1.5"/></svg>
    </div>
  </div>

  <section class="products">
    <div class="product"><div class="thumb"><div role="img" aria-label="Pencil cup with school supplies" style="background:linear-gradient(160deg,#f5c342,#e94b3c 60%,#3a9be0)"></div></div><div class="name">Lorem ipsum dolor</div><div class="row"><span class="price">$0.00</span><span class="add">ADD TO CART</span></div></div>
    <div class="product"><div class="thumb"><div role="img" aria-label="Apple with pencils and books" style="background:linear-gradient(160deg,#7dc242,#e94b3c 55%,#f5c342)"></div></div><div class="name">Lorem ipsum dolor</div><div class="row"><span class="price">$0.00</span><span class="add">ADD TO CART</span></div></div>
    <div class="product"><div class="thumb"><div role="img" aria-label="Fan of coloured pencils" style="background:linear-gradient(160deg,#3a9be0,#e94b3c 50%,#f5c342)"></div></div><div class="name">Lorem ipsum dolor</div><div class="row"><span class="price">$0.00</span><span class="add">ADD TO CART</span></div></div>
    <div class="product"><div class="thumb"><div role="img" aria-label="Pencil holder beside an apple" style="background:linear-gradient(160deg,#7dc242,#555 55%,#e94b3c)"></div></div><div class="name">Lorem ipsum dolor</div><div class="row"><span class="price">$0.00</span><span class="add">ADD TO CART</span></div></div>
    <div class="product"><div class="thumb"><div role="img" aria-label="Pencil cup with school supplies" style="background:linear-gradient(160deg,#f5c342,#e94b3c 60%,#3a9be0)"></div></div><div class="name">Lorem ipsum dolor</div><div class="row"><span class="price">$0.00</span><span class="add">ADD TO CART</span></div></div>
    <div class="product"><div class="thumb"><div role="img" aria-label="Apple with pencils and books" style="background:linear-gradient(160deg,#7dc242,#e94b3c 55%,#f5c342)"></div></div><div class="name">Lorem ipsum dolor</div><div class="row"><span class="price">$0.00</span><span class="add">ADD TO CART</span></div></div>
    <div class="product"><div class="thumb"><div role="img" aria-label="Fan of coloured pencils" style="background:linear-gradient(160deg,#3a9be0,#e94b3c 50%,#f5c342)"></div></div><div class="name">Lorem ipsum dolor</div><div class="row"><span class="price">$0.00</span><span class="add">ADD TO CART</span></div></div>
    <div class="product"><div class="thumb"><div role="img" aria-label="Pencil holder beside an apple" style="background:linear-gradient(160deg,#7dc242,#555 55%,#e94b3c)"></div></div><div class="name">Lorem ipsum dolor</div><div class="row"><span class="price">$0.00</span><span class="add">ADD TO CART</span></div></div>
  </section>
</main>

<footer class="footer"><div class="wrap">
  <div class="col">
    <h4>Our Contacts</h4>
    <ul class="contact">
      <li><svg viewBox="0 0 10 10"><path d="M5 1a3 3 0 0 1 3 3c0 2-3 5-3 5S2 6 2 4a3 3 0 0 1 3-3z" fill="#ccc"/></svg><span>12 Sample Street, Townsville</span></li>
      <li><svg viewBox="0 0 10 10"><path d="M2 1h2l1 2-1 1a6 6 0 0 0 2 2l1-1 2 1v2c-4 0-7-3-7-7z" fill="#ccc"/></svg><span>(00) 0000 0000</span></li>
      <li><svg viewBox="0 0 10 10"><rect x="1" y="2" width="8" height="6" fill="#ccc"/></svg><span>(00) 0000 0001</span></li>
      <li><svg viewBox="0 0 10 10"><rect x="1" y="2" width="8" height="6" fill="none" stroke="#ccc"/><path d="M1 2l4 3 4-3" fill="none" stroke="#ccc"/></svg><span>hello@ashfordlane.example</span></li>
    </ul>
  </div>
  <div class="col">
    <h4>About Us</h4>
    <p>Lorem ipsum dolor sit amet, consectetur adipiscing elit, sed do eiusmod tempor incididunt ut labore.</p>
  </div>
  <div class="col">
    <h4>Recent Tweets</h4>
    <p class="tweet">Lorem ipsum dolor sit amet, consectetur adipiscing elit.</p>
    <p class="tweet">Lorem ipsum dolor sit amet, consectetur adipiscing elit.</p>
  </div>
  <div class="col">
    <h4>Gallery</h4>
    <div class="gallery">
      <div role="img" aria-label="Classroom photo" style="background:#c9a77a"></div>
      <div role="img" aria-label="Classroom photo" style="background:#8fb3d6"></div>
      <div role="img" aria-label="Classroom photo" style="background:#d8c9b0"></div>
      <div role="img" aria-label="Classroom photo" style="background:#a6c98a"></div>
      <div role="img" aria-label="Classroom photo" style="background:#e0b36a"></div>
      <div role="img" aria-label="Classroom photo" style="background:#b9a6c9"></div>
    </div>
  </div>
</div></footer>
<div class="legal">Copyright 2014 Ashford Lane. All Rights Reserved. Disclaimer | Terms and Conditions | Privacy Policy</div>

</body>
</html>
```